" A empresa Modura BX nasceu com três pilares de negócios em seu ramo, que sao reforma, alugar e vender containers de valor agregado, container escritórios, almoxarifados, vestiários, banheiro, lojas ou projetos personalizados. "

```html
<!DOCTYPE html>
<html lang="pt-BR">
<head>
<meta charset="utf-8">
<title>Modura BX – Cartão de visita</title>
<link href="https://fonts.googleapis.com/css2?family=Jost:ital,wght@0,400;0,500;0,600;1,500;1,700&display=swap" rel="stylesheet">
<style>
  :root {
    --red: #c8202b;
    --blue: #1f3d73;
    --ink: #2b2b2b;
    --muted: #666666;
    --paper: #ffffff;
    --backdrop: #e4e4e4;
  }
  * { margin: 0; padding: 0; box-sizing: border-box; }
  html, body { width: 1200px; height: 1200px; overflow: hidden; }
  body {
    background: var(--backdrop);
    font-family: "Jost", sans-serif;
    color: var(--ink);
    position: relative;
  }
  .card {
    position: absolute;
    left: 150px;
    width: 900px;
    height: 500px;
    background: var(--paper);
    box-shadow: 0 6px 18px rgba(0,0,0,.12);
    overflow: hidden;
  }
  .card--contact { top: 70px; }
  .card--brand { top: 630px; }

  /* contact side */
  .side-bar {
    position: absolute; left: 0; top: 0; bottom: 0; width: 46px;
    background: var(--red);
    display: flex; flex-direction: column; justify-content: center; align-items: center; gap: 14px;
  }
  .side-bar svg { width: 18px; height: 18px; }
  .person { position: absolute; left: 96px; top: 74px; }
  .person__name { font-weight: 700; font-style: italic; font-size: 26px; color: var(--ink); }
  .person__role { font-style: italic; font-weight: 500; font-size: 16px; color: var(--muted); margin-top: 2px; }
  .contacts { position: absolute; left: 96px; top: 222px; list-style: none; }
  .contacts li { font-size: 22px; line-height: 34px; color: var(--blue); }
  .address {
    position: absolute; right: 54px; bottom: 70px; text-align: left;
    font-size: 21px; line-height: 30px; color: var(--blue);
  }

  /* company name block */
  .company { position: absolute; display: flex; align-items: center; }
  .company__dot { border-radius: 50%; background: var(--blue); flex: none; }
  .company__name { font-weight: 500; color: var(--blue); line-height: 1; }

  .card--contact .company { right: 54px; top: 150px; gap: 14px; }
  .card--contact .company__dot { width: 22px; height: 22px; }
  .card--contact .company__name { font-size: 44px; }

  .card--brand .company { left: 0; right: 0; top: 150px; justify-content: center; gap: 22px; }
  .card--brand .company__dot { width: 36px; height: 36px; }
  .card--brand .company__name { font-size: 72px; }

  .website {
    position: absolute; left: 0; right: 0; top: 330px; text-align: center;
    font-size: 26px; color: var(--blue); letter-spacing: .5px;
  }
  .base-band {
    position: absolute; left: 0; right: 0; bottom: 24px; height: 34px;
    background: var(--red);
  }
</style>
</head>
<body>

  <section class="card card--contact">
    <div class="side-bar">
      <svg viewBox="0 0 24 24" aria-hidden="true"><path fill="#fff" d="M6.6 10.8a15 15 0 0 0 6.6 6.6l2.2-2.2c.3-.3.7-.4 1-.2 1.1.4 2.3.6 3.6.6.6 0 1 .4 1 1V20c0 .6-.4 1-1 1A17 17 0 0 1 3 4c0-.6.4-1 1-1h3.5c.6 0 1 .4 1 1 0 1.3.2 2.5.6 3.6.1.3 0 .7-.2 1z"/></svg>
      <svg viewBox="0 0 24 24" aria-hidden="true"><rect x="7" y="2" width="10" height="20" rx="2" fill="#fff"/><rect x="9" y="5" width="6" height="11" fill="#c8202b"/></svg>
      <svg viewBox="0 0 24 24" aria-hidden="true"><rect x="2" y="5" width="20" height="14" rx="1" fill="#fff"/><path d="M3 6l9 7 9-7" fill="none" stroke="#c8202b" stroke-width="2"/></svg>
      <svg viewBox="0 0 24 24" aria-hidden="true"><circle cx="12" cy="12" r="9" fill="#fff"/></svg>
    </div>

    <div class="person">
      <p class="person__name">Rafael Tavares</p>
      <p class="person__role">Advogado</p>
    </div>

    <ul class="contacts">
      <li>11 3400-1275</li>
      <li>11 8500-4310</li>
      <li>contato@modurabx.com.br</li>
      <li>/modurabx</li>
    </ul>

    <div class="company">
      <span class="company__dot"></span>
      <p class="company__name">Modura BX</p>
    </div>

    <p class="address">Av. Joaquim Ribeiro Prado<br>nº 214 | Vila Serena | Santa Aurora | SP</p>
  </section>

  <section class="card card--brand">
    <div class="company">
      <span class="company__dot"></span>
      <p class="company__name">Modura BX</p>
    </div>
    <p class="website">www.modurabx.com.br</p>
    <div class="base-band"></div>
  </section>

</body>
</html>
```